Design cover for information booklet
I am looking for a design for the front and back cover of an information booklet. Also an inside page basic design.
The booklet will contain 10 double sided pages providing information on weight loss surgery.
See my website www.brevinmarsh.com.au for what I do and typical colour themes.
I would also like some theming/illustration which can be utilised on each inside page of the booklet, rather than the pages just being blank with text etc. What would a blank page on this inside of the booklet look like under the design theme that you have created?
My company is Kestrel Institute for Metabolic Surgery. You will find uploaded a Logo for Kestrel Institute for Metabolic Surgery as well as my other logo which is my name “Brevin Marsh, etc.”. The Kestrel Institute for Metabolic Surgery logo should be utilised. The other logo (Brevin Marsh) is optional.
The front cover should contain the following text as minimum:
Kestrel Institute for Metabolic Surgery
Mr Brevin Marsh MBBS FRACS GradCert (Health Stats)
Our tagline is “Experience, Expertise and Empathy”. This should probably be on the front cover also.
The back cover contains (as a minimum) our address, phone number, fax number:
Suite 17, Level 3
Tallowgate Northern Hospital
9 Pemberly Road, Fernwick VIC 3174
Phone: 03 9412 6083
Fax: 03 9417 2865
Email: info@kestrelims.com.au
The files should be in a form whereby the text can be edited and changed if need be.
1. problems with initial graphical attachments - Artforge end 2. several requests by designers for extension

```html
<!DOCTYPE html>
<html lang="en">
<head>
<meta charset="utf-8">
<title>Kestrel Institute for Metabolic Surgery – Booklet Covers and Inside Spread</title>
<link rel="stylesheet" href="https://fonts.googleapis.com/css2?family=Tinos:wght@400&family=Lato:wght@400;700&display=swap">
<style>
  :root{
    --teal:#177a6f;
    --teal-dark:#0f5f56;
    --grey:#77787b;
    --grey-light:#b9bbbd;
    --panel:#ececec;
    --paper:#ffffff;
    --stage:#eceef0;
    --ink:#5a5b5d;
    --serif:"Tinos", "Times New Roman", serif;
    --sans:"Lato", Arial, sans-serif;
  }
  *{margin:0;padding:0;box-sizing:border-box}
  html,body{width:910px;height:1200px;overflow:hidden;background:var(--stage)}
  body{position:relative;font-family:var(--sans);color:var(--ink)}

  .spread{position:absolute;left:105px;width:692px;background:var(--paper);overflow:hidden}
  .spread--covers{top:74px;height:491px}
  .spread--inside{top:630px;height:489px}
  .spread::after{content:"";position:absolute;left:334px;top:0;width:24px;height:100%;
    background:linear-gradient(90deg,rgba(0,0,0,0) 0%,rgba(0,0,0,.08) 48%,rgba(0,0,0,0) 100%);pointer-events:none}

  .abs{position:absolute}
  .photo{position:absolute}

  /* ---------- covers ---------- */
  .cover-top-shapes{position:absolute;left:0;top:0;width:692px;height:111px}
  .photo--family{left:0;top:0;width:206px;height:111px;
    background:linear-gradient(100deg,#c9cfd2 0%,#d8d2c6 40%,#9a8a78 65%,#cfd6da 100%)}
  .back-panel{left:0;top:111px;width:346px;height:239px;background:var(--teal)}
  .photo--theatre{left:346px;top:111px;width:346px;height:239px;
    background:linear-gradient(120deg,#9fb6d3 0%,#6f8fbd 35%,#4d6fa0 60%,#a9bed8 100%)}

  .panel-col{position:absolute;top:146px;color:#fff}
  .panel-col--a{left:16px;width:159px}
  .panel-col--b{left:186px;width:150px}
  .panel-heading{font-family:var(--serif);font-size:10px;font-weight:400;padding-bottom:5px;
    border-bottom:.6px solid rgba(255,255,255,.8);margin-bottom:6px;width:96%}
  .panel-col--b .panel-heading{width:100%}
  .panel-text{font-size:5.6px;line-height:8.2px;text-align:justify;margin-bottom:8px}
  .panel-col--b .panel-text{padding-left:5px}

  .brand{position:absolute;display:flex;align-items:center;gap:6px}
  .brand__square{background:var(--teal)}
  .brand__name{font-family:var(--serif);font-weight:400;color:var(--teal);line-height:1.05}
  .brand--back{left:25px;top:406px}
  .brand--back .brand__square{width:30px;height:30px}
  .brand--back .brand__name{font-size:9.5px}
  .brand--front{left:455px;top:35px}
  .brand--front .brand__square{width:43px;height:43px}
  .brand--front .brand__name{font-size:13px}

  .contact-list{position:absolute;left:264px;top:389px;width:80px;list-style:none}
  .contact-item{display:flex;align-items:flex-start;gap:6px;font-size:6.4px;line-height:8px;color:#333;margin-bottom:4px;white-space:nowrap}
  .contact-icon{flex:0 0 7px;width:7px;height:7px;margin-top:0.5px}

  .tagline{position:absolute;left:346px;width:346px;top:378px;text-align:center;
    font-family:var(--serif);color:var(--teal);font-size:22px;line-height:26px;font-weight:400}
  .credentials{position:absolute;left:346px;width:346px;top:434px;text-align:center;font-size:7.4px;color:var(--grey)}

  .footer-bar{position:absolute;top:465px;height:26px;width:346px}
  .footer-bar--back{left:0}
  .footer-bar--front{left:346px}
  .footer-bar > .footer-shape{position:absolute;left:0;top:0}
  .footer-web,.footer-phone{position:absolute;top:0;height:26px;font-size:7.6px;line-height:1;color:#fff;display:flex;align-items:center;gap:5px;white-space:nowrap}
  .footer-web{left:17px}
  .footer-phone{left:213px}
  .footer-icon{flex:0 0 8px;width:8px;height:8px}

  /* ---------- inside spread ---------- */
  .intro-block{left:0;top:0;width:209px;height:125px;background:var(--teal)}
  .intro-title{position:absolute;left:12px;top:93px;font-family:var(--serif);font-size:12.5px;line-height:16px;color:#fff;font-weight:400}
  .photo--portrait{left:209px;top:0;width:126px;height:125px;
    background:radial-gradient(circle at 50% 55%,#4a4a4c 0%,#1d1d1f 60%,#0b0b0c 100%)}
  .about-panel{left:209px;top:125px;width:126px;height:364px;background:var(--panel)}
  .spine-accent{left:335px;top:125px;width:11px;height:32px;background:var(--teal-dark)}
  .photo--team{left:0;top:353px;width:208px;height:136px;
    background:linear-gradient(110deg,#e7edf2 0%,#c8d5e0 45%,#8ea4b8 75%,#dfe6ec 100%)}
  .photo--surgeons{left:346px;top:0;width:346px;height:125px;
    background:linear-gradient(100deg,#6d7f95 0%,#8a9ab0 30%,#3f5f8f 60%,#d9dde2 100%)}

  .text-col{position:absolute}
  .body-text{font-size:5.9px;line-height:8.3px;text-align:justify;color:var(--ink)}
  .section-heading{font-size:7.2px;line-height:9.4px;color:var(--teal);font-weight:400;margin-bottom:3px}

  .col-intro{left:12px;top:152px;width:171px}
  .col-intro .section-heading{margin-top:27px}

  .col-about{left:219px;top:152px;width:108px}
  .col-about .section-heading{font-size:7.2px;margin-bottom:3px}
  .col-about .body-text{font-size:6.1px;line-height:8.2px;margin-bottom:9px;color:#666}

  .col-right-a{left:366px;top:153px;width:141px}
  .col-right-b{left:533px;top:153px;width:140px}
  .col-right-a .body-text,.col-right-b .body-text{margin-bottom:8px}
  .col-right-a .gap-heading{margin-top:28px}
  .highlight-box{background:var(--teal);padding:5px 6px;margin:12px 0 14px}
  .highlight-box .body-text{color:#fff;margin:0}
</style>
</head>
<body>

<!-- Back and front cover -->
<section class="spread spread--covers" aria-label="Back and front cover">
  <svg class="cover-top-shapes" viewBox="0 0 692 111" width="692" height="111">
    <defs>
      <linearGradient id="coverSheen" x1="0" x2="1" y1="0" y2="0">
        <stop offset="0" stop-color="#ffffff"/>
        <stop offset="1" stop-color="#eeeeee"/>
      </linearGradient>
    </defs>
    <rect x="346" y="0" width="346" height="111" fill="url(#coverSheen)"/>
    <polygon points="206,0 330,0 460,111 206,111" fill="#177a6f"/>
    <polygon points="330,0 352,0 482,111 460,111" fill="#a7a9ab"/>
  </svg>
  <div class="photo photo--family" role="img" aria-label="Photo of a father and son hugging on a beach"></div>

  <div class="brand brand--front">
    <span class="brand__square"></span>
    <span class="brand__name">Kestrel Institute<br>for Metabolic Surgery</span>
  </div>

  <div class="abs back-panel"></div>
  <div class="panel-col panel-col--a">
    <h3 class="panel-heading">Weight Loss Surgery.</h3>
    <p class="panel-text">Weight loss surgery can change your health and daily life. Our team will guide you through each step, from your first visit to long term care and support after the procedure. Ask us about diet, exercise and follow up visits so you feel ready and well informed.</p>
    <p class="panel-text">Each patient is different. We look at your history, your goals and your lifestyle before we suggest the option that suits you best.</p>
    <p class="panel-text">Ask us about diet, exercise and follow up visits so you feel ready and well informed.</p>
  </div>
  <div class="panel-col panel-col--b">
    <h3 class="panel-heading">Which Operation is best for me?</h3>
    <p class="panel-text">Each patient is different. We look at your history, your goals and your lifestyle before we suggest the option that suits you best. Ask us about diet, exercise and follow up visits so you feel ready and well informed.</p>
    <p class="panel-text">Weight loss surgery can change your health and daily life. Our team will guide you through each step, from your first visit to long term care and support after the procedure.</p>
    <p class="panel-text">Each patient is different. We look at your history, your goals and your lifestyle before we suggest the option that suits you best.</p>
  </div>

  <div class="photo photo--theatre" role="img" aria-label="Photo of a surgical team operating in theatre"></div>

  <div class="brand brand--back">
    <span class="brand__square"></span>
    <span class="brand__name">Kestrel Institute<br>for Metabolic Surgery</span>
  </div>

  <ul class="contact-list">
    <li class="contact-item">
      <svg class="contact-icon" viewBox="0 0 10 10"><rect x="0.5" y="1.5" width="9" height="7" rx="1.5" fill="none" stroke="#8a8b8d"/><path d="M1 2.5 L5 5.5 L9 2.5" fill="none" stroke="#8a8b8d"/></svg>
      <span>info@kestrelims.com.au</span>
    </li>
    <li class="contact-item">
      <svg class="contact-icon" viewBox="0 0 10 10"><rect x="0.5" y="0.5" width="9" height="9" rx="2" fill="none" stroke="#8a8b8d"/><circle cx="5" cy="5" r="2" fill="none" stroke="#8a8b8d"/></svg>
      <span>www.brevinmarsh.com.au</span>
    </li>
    <li class="contact-item">
      <svg class="contact-icon" viewBox="0 0 10 10"><path d="M5 9.5 C2 6 1.5 4.8 1.5 3.8 A3.5 3.5 0 0 1 8.5 3.8 C8.5 4.8 8 6 5 9.5Z" fill="#8a8b8d"/><circle cx="5" cy="3.8" r="1.2" fill="#fff"/></svg>
      <span>Suite 17, Level 3<br>Tallowgate Northern Hospital<br>9 Pemberly Road, Fernwick VIC 3174</span>
    </li>
    <li class="contact-item">
      <svg class="contact-icon" viewBox="0 0 10 10"><circle cx="5" cy="5" r="4.5" fill="#8a8b8d"/><path d="M3.3 2.5 L4.3 3.8 L3.8 4.4 C4.3 5.3 4.8 5.8 5.6 6.2 L6.2 5.7 L7.5 6.7 L6.9 7.6 C4.8 7.4 2.6 5.2 2.4 3.1Z" fill="#fff"/></svg>
      <span>Phone: 03 9412 6083<br>Fax: 03 9417 2865</span>
    </li>
  </ul>

  <h1 class="tagline">EXPERIENCE,<br>EXPERTISE &amp; EMPATHY</h1>
  <p class="credentials">Mr Brevin Marsh MBBS FRACS GradCert (Health Stats)</p>

  <div class="footer-bar footer-bar--back">
    <svg class="footer-shape" viewBox="0 0 346 26" width="346" height="26">
      <rect width="346" height="26" fill="#77787b"/>
      <polygon points="0,0 170,0 180,26 0,26" fill="#177a6f"/>
      <polygon points="170,0 174,0 184,26 180,26" fill="#ffffff"/>
    </svg>
    <span class="footer-web"><svg class="footer-icon" viewBox="0 0 10 10"><circle cx="5" cy="5" r="4.5" fill="#fff"/><path d="M0.8 5 H9.2 M5 0.6 V9.4 M5 0.6 C2.5 3 2.5 7 5 9.4 M5 0.6 C7.5 3 7.5 7 5 9.4" fill="none" stroke="#177a6f" stroke-width=".8"/></svg>www.brevinmarsh.com.au</span>
    <span class="footer-phone"><svg class="footer-icon" viewBox="0 0 10 10"><circle cx="5" cy="5" r="4.5" fill="#fff"/><path d="M3.3 2.5 L4.3 3.8 L3.8 4.4 C4.3 5.3 4.8 5.8 5.6 6.2 L6.2 5.7 L7.5 6.7 L6.9 7.6 C4.8 7.4 2.6 5.2 2.4 3.1Z" fill="#77787b"/></svg>(03) 9412 6083</span>
  </div>
  <div class="footer-bar footer-bar--front">
    <svg class="footer-shape" viewBox="0 0 346 26" width="346" height="26">
      <rect width="346" height="26" fill="#77787b"/>
      <polygon points="0,0 170,0 180,26 0,26" fill="#177a6f"/>
      <polygon points="170,0 174,0 184,26 180,26" fill="#ffffff"/>
    </svg>
    <span class="footer-web"><svg class="footer-icon" viewBox="0 0 10 10"><circle cx="5" cy="5" r="4.5" fill="#fff"/><path d="M0.8 5 H9.2 M5 0.6 V9.4 M5 0.6 C2.5 3 2.5 7 5 9.4 M5 0.6 C7.5 3 7.5 7 5 9.4" fill="none" stroke="#177a6f" stroke-width=".8"/></svg>www.brevinmarsh.com.au</span>
    <span class="footer-phone"><svg class="footer-icon" viewBox="0 0 10 10"><circle cx="5" cy="5" r="4.5" fill="#fff"/><path d="M3.3 2.5 L4.3 3.8 L3.8 4.4 C4.3 5.3 4.8 5.8 5.6 6.2 L6.2 5.7 L7.5 6.7 L6.9 7.6 C4.8 7.4 2.6 5.2 2.4 3.1Z" fill="#77787b"/></svg>(03) 9412 6083</span>
  </div>
</section>

<!-- Inside pages -->
<section class="spread spread--inside" aria-label="Inside page spread">
  <div class="abs intro-block"></div>
  <h2 class="intro-title">General, Upper GI<br>&amp; Bariatric Surgeon</h2>
  <div class="photo photo--portrait" role="img" aria-label="Portrait photo of the surgeon in a suit"></div>
  <div class="abs about-panel"></div>
  <div class="abs spine-accent"></div>

  <div class="text-col col-intro">
    <p class="body-text">Weight loss surgery can change your health and daily life. Our team will guide you through each step, from your first visit to long term care and support after the procedure. Each patient is different. We look at your history, your goals and your lifestyle before we suggest the option that suits you best.</p>
    <h3 class="section-heading">Weight Loss Surgery.</h3>
    <p class="body-text">Weight loss surgery can change your health and daily life. Our team will guide you through each step, from your first visit to long term care and support after the procedure. Each patient is different. We look at your history, your goals and your lifestyle before we suggest the option that suits you best. Ask us about diet, exercise and follow up visits so you feel ready and well informed.</p>
  </div>

  <div class="photo photo--team" role="img" aria-label="Photo of a doctor consulting with a couple"></div>

  <div class="text-col col-about">
    <h3 class="section-heading">A Little About Us</h3>
    <p class="body-text">Mr Marsh is a Melbourne based General, Upper GI &amp; Bariatric specialist with an interest in minimally invasive and robotic surgery. With two years of specialty Fellowship training in Upper GI &amp; Bariatric Procedures and a high volume bariatric practice his training and experience in weight loss surgery is amongst the very best in Australia.</p>
    <p class="body-text">Bariatric operations include sleeve gastrectomy (also known as gastric sleeve or sleeve gastric), gastric bypass, gastric banding, revisional surgery, Enteroline implantation &amp; Lumora Balloon. In addition to bariatric procedures Mr Marsh performs antireflux as well as endoscopic procedures including gastroscopy &amp; colonoscopy and a range of general surgery including gallbladder, hernia, small and large bowel and minor procedures. Abdominoplasty (tummy tuck) and brachioplasty (arm reduction) are offered as body contouring procedures for weight loss patients.</p>
    <p class="body-text">The above procedures are generally performed using minimally invasive or keyhole approaches. Robotic technology is employed to assist with gastric bypass and revisional procedures where feasible.</p>
  </div>

  <div class="photo photo--surgeons" role="img" aria-label="Photo of two surgeons in scrubs and caps"></div>

  <div class="text-col col-right-a">
    <h3 class="section-heading">Weight Loss Surgery.</h3>
    <p class="body-text">Weight loss surgery can change your health and daily life. Our team will guide you through each step, from your first visit to long term care and support after the procedure. Each patient is different. We look at your history, your goals and your lifestyle before we suggest the option that suits you best.</p>
    <h3 class="section-heading gap-heading">Weight Loss Surgery.</h3>
    <p class="body-text">Weight loss surgery can change your health and daily life. Our team will guide you through each step, from your first visit to long term care and support after the procedure. Each patient is different. We look at your history, your goals and your lifestyle before we suggest the option that suits you best. Ask us about diet, exercise and follow up visits so you feel ready and well informed.</p>
    <p class="body-text">Weight loss surgery can change your health and daily life. Our team will guide you through each step, from your first visit to long term care and support after the procedure.</p>
  </div>

  <div class="text-col col-right-b">
    <h3 class="section-heading">Weight Loss Surgery.<br>Which Operation is best for me?</h3>
    <p class="body-text">Weight loss surgery can change your health and daily life. Our team will guide you through each step, from your first visit to long term care and support after the procedure. Each patient is different. We look at your history, your goals and your lifestyle before we suggest the option that suits you best. Ask us about diet, exercise and follow up visits so you feel ready and well informed.</p>
    <div class="highlight-box">
      <p class="body-text">Weight loss surgery can change your health and daily life. Our team will guide you through each step, from your first visit to long term care and support after the procedure.</p>
    </div>
    <h3 class="section-heading">Which Operation is best for me?</h3>
    <p class="body-text">Weight loss surgery can change your health and daily life. Our team will guide you through each step, from your first visit to long term care and support after the procedure. Each patient is different. We look at your history, your goals and your lifestyle before we suggest the option that suits you best.</p>
  </div>
</section>

</body>
</html>
```